Conceptual Model Diagram for Replacing Medication with Behavior to Support Weight Loss Maintenance

Design a figure of a conceptual model that needs to be inserted into a word document for a PSF grant. This conceptual model illustrates how behavioral strategies can replace the regulatory functions lost after AOM discontinuation. The intervention targets three core vulnerabilities—appetite resurgence, metabolic inflexibility, and suboptimal mindstate—through the domains of Food, Physical Activity, and Mind. Sustained weight loss maintenance occurs at the intersection of these domains. The intervention is delivered within a design framework that makes behaviors easier to perform, aligns them with identity, and reinforces them through virtual support and community, ensuring real-world feasibility and long-term adherence.
Target Market(s)
PSF reviewers
Industry/Entity Type
academic
Other font styles liked:
- arial
Requirements
Must have
- see my attached description

```html
<!DOCTYPE html>
<html lang="en">
<head>
<meta charset="utf-8">
<title>Replacing Medicine with Behavior for Weight Loss – Conceptual Model</title>
<link href="https://fonts.googleapis.com/css2?family=Arimo:wght@400;700&family=Roboto+Condensed:wght@400&display=swap" rel="stylesheet">
<style>
  :root {
    --ink: #231f20;
    --title-grey: #5a5a5a;
    --mind: #f9d9bf;
    --mind-accent: #e07b1c;
    --food: #c0bcd6;
    --food-accent: #261a6b;
    --activity: #b6e0f4;
    --activity-accent: #0a8fd8;
    --mind-food: #bd9fa4;
    --mind-activity: #b2c4c7;
    --food-activity: #8aaed8;
    --core: #8a9db5;
    --core-text: #fff200;
    --callout-head: #d42a27;
    --paper: #ffffff;
  }
  html, body { margin: 0; padding: 0; overflow: hidden; background: var(--paper); }
  .canvas { width: 1200px; height: 899px; position: relative; overflow: hidden; }
  .model { display: block; width: 1200px; height: 899px; }
  .model text { font-family: "Arimo", Arial, sans-serif; }
  .model .diagram-title { font-family: "Roboto Condensed", "Arial Narrow", sans-serif; font-size: 29px; fill: var(--title-grey); }
  .model .diagram-title .small-caps { font-size: 21px; }
  .domain-label { font-size: 20px; font-weight: 700; fill: var(--ink); }
  .core-label { font-size: 9.5px; font-weight: 700; fill: var(--core-text); }
  .vulnerability { font-size: 22px; font-weight: 700; }
  .vulnerability.mind { fill: var(--mind-accent); }
  .vulnerability.food { fill: var(--food-accent); }
  .vulnerability.activity { fill: var(--activity-accent); }
  .callout-head { font-size: 14px; font-weight: 700; fill: var(--callout-head); }
  .callout-body { font-size: 13.5px; fill: var(--ink); }
  .callout-frame { fill: var(--paper); stroke-width: 1.2; }
  .domain-ring { fill: none; stroke-width: 2.6; stroke-dasharray: 5 3.5; }
</style>
</head>
<body>
<div class="canvas">
<svg class="model" viewBox="0 0 1200 899" xmlns="http://www.w3.org/2000/svg" role="img" aria-label="Conceptual model: Mind, Food and Physical Activity overlap to produce sustained weight loss maintenance">
  <defs>
    <clipPath id="clip-mind"><circle cx="600" cy="458" r="113"/></clipPath>
    <clipPath id="clip-food"><circle cx="529" cy="589" r="114"/></clipPath>
    <clipPath id="clip-activity"><circle cx="671" cy="589" r="114"/></clipPath>
    <marker id="head-mind" markerWidth="8" markerHeight="8" refX="4" refY="4" orient="auto" markerUnits="userSpaceOnUse" viewBox="0 0 8 8"><path d="M0,0 L8,4 L0,8 z" fill="var(--mind-accent)"/></marker>
  </defs>

  <!-- Title -->
  <text class="diagram-title" x="600" y="97" text-anchor="middle">DIAGRAM <tspan class="small-caps">OF</tspan> REPLACING MEDICINE <tspan class="small-caps">WITH</tspan> BEHAVIOR <tspan class="small-caps">FOR</tspan> WEIGHT LOSS</text>
  <line x1="220" y1="103" x2="979" y2="103" stroke="var(--title-grey)" stroke-width="1.5"/>

  <!-- Dashed domain rings -->
  <path class="domain-ring" d="M472,468 A128,128 0 1 1 727,468" stroke="var(--mind-accent)"/>
  <path class="domain-ring" d="M468,476 A128,128 0 1 0 596,700" stroke="var(--food-accent)"/>
  <path class="domain-ring" d="M730,476 A128,128 0 1 1 603,697" stroke="var(--activity-accent)"/>

  <!-- Domains -->
  <g class="venn">
    <circle cx="600" cy="458" r="113" fill="var(--mind)"/>
    <circle cx="529" cy="589" r="114" fill="var(--food)"/>
    <circle cx="671" cy="589" r="114" fill="var(--activity)"/>
    <g clip-path="url(#clip-mind)">
      <circle cx="529" cy="589" r="114" fill="var(--mind-food)"/>
      <circle cx="671" cy="589" r="114" fill="var(--mind-activity)"/>
    </g>
    <g clip-path="url(#clip-food)">
      <circle cx="671" cy="589" r="114" fill="var(--food-activity)"/>
    </g>
    <g clip-path="url(#clip-mind)"><g clip-path="url(#clip-food)">
      <circle cx="671" cy="589" r="114" fill="var(--core)"/>
    </g></g>
    <g fill="none" stroke="var(--paper)" stroke-width="2">
      <circle cx="600" cy="458" r="113"/>
      <circle cx="529" cy="589" r="114"/>
      <circle cx="671" cy="589" r="114"/>
    </g>
  </g>

  <!-- Domain labels -->
  <text class="domain-label" x="600" y="413" text-anchor="middle">MIND</text>
  <text class="domain-label" x="492" y="633" text-anchor="middle">FOOD</text>
  <text class="domain-label" x="711" y="616" text-anchor="middle">PHYSICAL</text>
  <text class="domain-label" x="711" y="638" text-anchor="middle">ACTIVITY</text>
  <text class="core-label" text-anchor="middle"><tspan x="600" y="539">Sustained</tspan><tspan x="600" y="551">Weight Loss</tspan><tspan x="600" y="563">Maintenance</tspan></text>

  <!-- Vulnerability arrows -->
  <line x1="600" y1="371" x2="600" y2="262" stroke="var(--mind-accent)" stroke-width="2"/>
  <path d="M594,266 L600,253 L606,266 z" fill="var(--mind-accent)"/>
  <line x1="476" y1="645" x2="400" y2="721" stroke="var(--food-accent)" stroke-width="2"/>
  <path d="M393,728 L398,714 L407,723 z" fill="var(--food-accent)"/>
  <line x1="730" y1="653" x2="806" y2="729" stroke="var(--activity-accent)" stroke-width="2"/>
  <path d="M813,736 L799,731 L808,722 z" fill="var(--activity-accent)"/>

  <!-- Vulnerabilities -->
  <text class="vulnerability mind" text-anchor="middle"><tspan x="600" y="218">Suboptimal</tspan><tspan x="600" y="247">Mindstate</tspan></text>
  <text class="vulnerability food" text-anchor="middle"><tspan x="383" y="761">Appetite</tspan><tspan x="383" y="786">Resurgence</tspan></text>
  <text class="vulnerability activity" text-anchor="middle"><tspan x="822" y="761">Metabolic</tspan><tspan x="822" y="786">Inflexibility</tspan></text>

  <!-- Callout: virtual support -->
  <path class="callout-frame" stroke="var(--mind-accent)" d="M306,261 H475 Q481,261 481,267 V327 Q481,333 475,333 H460 L502,373 L438,333 H306 Q300,333 300,327 V267 Q300,261 306,261 z"/>
  <text class="callout-head" text-anchor="middle"><tspan x="391" y="279">VIRTUAL SUPPORT AND</tspan><tspan x="391" y="295">SOCIAL CONNECTION</tspan></text>
  <text class="callout-body" text-anchor="middle"><tspan x="391" y="311">Accessibility, Community,</tspan><tspan x="391" y="327">Shared Accountability</tspan></text>

  <!-- Callout: make it easy -->
  <path class="callout-frame" stroke="var(--food-accent)" d="M211,476 H370 Q376,476 376,482 V542 Q376,548 370,548 H358 L400,588 L336,548 H211 Q205,548 205,542 V482 Q205,476 211,476 z"/>
  <text class="callout-head" x="290" y="497" text-anchor="middle">MAKE IT EASY</text>
  <text class="callout-body" text-anchor="middle"><tspan x="290" y="513">Habits, Routines,</tspan><tspan x="290" y="529">Environment, Low friction</tspan></text>

  <!-- Callout: identity -->
  <path class="callout-frame" stroke="var(--activity-accent)" d="M830,476 H989 Q995,476 995,482 V542 Q995,548 989,548 H864 L801,588 L843,548 H830 Q824,548 824,542 V482 Q824,476 830,476 z"/>
  <text class="callout-head" x="909" y="500" text-anchor="middle">ALIGN WITH IDENTITY</text>
  <text class="callout-body" text-anchor="middle"><tspan x="909" y="516">Self-concept, Maintain IT</tspan><tspan x="909" y="532">model, Internalization)</tspan></text>
</svg>
</div>
</body>
</html>
```